Business card design

Hi,
I need to have a business card design based on the current logo.
If competitive I not put it out to everyone.

It can be single of double sided

Target Market(s)

Food businesses

Industry/Entity Type

Food Manufacturing

Contact Information for Business Card

Details will on card will be as follows Name = Marcus Helt Email = Marcus@TalBakery.com.au Phone = 0418562207 Address = 17 Lanford Street , Fortitude Valley QLD 4006 Australia

Font styles to use
Other font styles liked:
• based on two fonts - Adelle & Museo

Requirements
Must have
• Based on the on switch concept

```html
<!DOCTYPE html>
<html lang="en">
<head>
<meta charset="utf-8">
<title>Tal Bakery – Business Card</title>
<link href="https://fonts.googleapis.com/css2?family=Open+Sans:wght@400;700&family=Zilla+Slab:wght@600&display=swap" rel="stylesheet">
<style>
  :root {
    --backdrop: #dedbda;
    --card: #f4f3f3;
    --brand-red: #e02342;
    --ink-dark: #2e2223;
    --ink-grey: #4a4a4a;
  }
  * { margin: 0; padding: 0; box-sizing: border-box; }
  html, body {
    width: 1200px; height: 1200px; overflow: hidden;
    background: var(--backdrop);
  }
  .sheet {
    width: 1200px; height: 1200px;
    display: flex; flex-direction: column;
    align-items: center; justify-content: center; gap: 80px;
  }
  .card {
    width: 700px; height: 428px;
    background: var(--card);
    position: relative;
    box-shadow: 0 10px 30px rgba(0,0,0,0.12);
  }
  /* Front */
  .card-front {
    display: flex; align-items: center; justify-content: center;
  }
  .lockup { display: flex; flex-direction: column; align-items: flex-start; }
  .wordmark-row { display: flex; align-items: center; gap: 18px; }
  .brand-dot {
    flex: none;
    width: 58px; height: 58px; border-radius: 50%;
    background: var(--brand-red);
  }
  .wordmark {
    font-family: "Open Sans", sans-serif; font-weight: 700;
    font-size: 64px; line-height: 1; color: var(--ink-dark);
    letter-spacing: 1px; white-space: nowrap;
  }
  .tagline {
    font-family: "Zilla Slab", serif; font-weight: 600;
    font-size: 24px; color: var(--ink-dark);
    margin: 8px 0 0 76px; white-space: nowrap;
  }
  /* Back */
  .card-back {
    display: flex; align-items: center;
    padding: 0 50px 0 60px; gap: 40px;
  }
  .back-mark { display: flex; align-items: center; gap: 12px; flex: none; }
  .back-mark .brand-dot { width: 44px; height: 44px; }
  .back-mark .wordmark { font-size: 38px; color: var(--brand-red); letter-spacing: 0; }
  .contact {
    font-family: "Open Sans", sans-serif; color: var(--ink-grey);
    font-size: 16px; line-height: 1.45; white-space: nowrap;
  }
  .contact-name {
    font-weight: 700; font-size: 30px; color: var(--brand-red);
    line-height: 1.1; margin-bottom: 4px;
  }
  .contact-address { margin-top: 34px; }
  .contact-web { font-weight: 700; color: var(--brand-red); font-size: 17px; }
</style>
</head>
<body>
  <main class="sheet">
    <section class="card card-front">
      <div class="lockup">
        <div class="wordmark-row">
          <span class="brand-dot"></span>
          <span class="wordmark">Tal Bakery</span>
        </div>
        <p class="tagline">Fresh Baked Goods Daily</p>
      </div>
    </section>

    <section class="card card-back">
      <div class="back-mark">
        <span class="brand-dot"></span>
        <span class="wordmark">Tal Bakery</span>
      </div>
      <div class="contact">
        <p class="contact-name">Marcus Helt</p>
        <p class="contact-email">Marcus@TalBakery.com.au</p>
        <p class="contact-phone">0418562207</p>
        <p class="contact-address">17 Lanford Street , Kelvin Grove<br>QLD 4059 Australia</p>
        <p class="contact-web">www.talbakery.com.au</p>
      </div>
    </section>
  </main>
</body>
</html>
```